KLT Business cards & stationary
Business cards and stationary
Project: KLT Business cards & stationary
KLT Business cards & stationary - Real Estate
Creative Brief
Use same font as used in my logo
Im not sure if my logo font will look good
Professional
Marcus Pellow
President
42 Tarrow Lane Suite 115 East Orange, NJ 07019
Marcus@marcusprealtyco.example
MarcusPrealtyco.example
company name on business card
marcusp marcusp
i definitely want to promote the website address on the card in a classy way also the company name should appear along with logo on the front

```html
<!DOCTYPE html>
<html lang="en">
<head>
<meta charset="utf-8">
<title>KLT Business Card – Marcus Pellow</title>
<link href="https://fonts.googleapis.com/css2?family=Cinzel:wght@400;600&family=Open+Sans:wght@400;600&display=swap" rel="stylesheet">
<style>
  :root{
    --bg:#e6e8eb;
    --paper:#ffffff;
    --blue:#1f5fae;
    --blue-dark:#173f7a;
    --blue-light:#3f86d6;
    --grey:#8c9096;
    --grey-light:#b4b7bb;
    --ink:#4a4d52;
  }
  *{box-sizing:border-box;margin:0;padding:0}
  html,body{width:1200px;height:840px;overflow:hidden;background:var(--bg)}
  .canvas{position:relative;width:1200px;height:840px}
  .card{position:absolute;top:265px;width:540px;height:309px;overflow:hidden;box-shadow:0 6px 18px rgba(0,0,0,.18)}
  .card--front{left:40px;background:var(--paper)}
  .card--back{left:620px;background:linear-gradient(180deg,var(--blue-light) 0%,var(--blue) 45%,var(--blue-dark) 100%)}

  /* front */
  .front__rule{position:absolute;left:0;right:0;top:58px;height:2px;background:var(--blue)}
  .front__name{position:absolute;right:58px;top:24px;font-family:"Cinzel",serif;font-size:25px;color:var(--blue);letter-spacing:.5px}
  .front__accent{position:absolute;right:44px;top:22px;width:4px;height:62px;background:var(--blue)}
  .front__title{position:absolute;right:58px;top:66px;font-family:"Open Sans",sans-serif;font-size:9px;letter-spacing:2px;color:var(--ink)}
  .brand{position:absolute;left:40px;top:74px;text-align:center;width:130px}
  .brand__mark{width:30px;height:30px;border-radius:50%;background:var(--blue);margin:0 auto 4px}
  .brand__name{font-family:"Cinzel",serif;font-size:19px;color:var(--blue)}
  .brand__tag{font-family:"Open Sans",sans-serif;font-size:7px;letter-spacing:3px;color:var(--grey)}
  .front__band{position:absolute;left:0;top:0}
  .contact{position:absolute;top:218px;font-family:"Open Sans",sans-serif;font-size:8.5px;line-height:1.55;color:var(--ink)}
  .contact--address{left:52px;width:120px}
  .contact--phone{left:236px}
  .contact--web{left:386px}

  /* back */
  .back__brand{position:absolute;right:40px;top:34px;display:flex;align-items:center;gap:10px}
  .back__mark{width:30px;height:30px;border-radius:50%;background:#ffffff}
  .back__brandname{font-family:"Cinzel",serif;font-size:20px;color:#ffffff}
  .back__band{position:absolute;left:0;right:0;top:140px;height:56px;background:var(--grey)}
  .back__stripe{position:absolute;left:0;right:0;top:196px;height:6px;background:var(--grey-light)}
  .back__name{position:absolute;left:40px;top:150px;font-family:"Cinzel",serif;font-size:22px;color:#ffffff}
  .back__title{position:absolute;left:40px;top:178px;font-family:"Open Sans",sans-serif;font-size:8px;letter-spacing:2px;color:#f2f2f2}
</style>
</head>
<body>
<div class="canvas">

  <section class="card card--front">
    <div class="front__rule"></div>
    <div class="front__name">MARCUS PELLOW</div>
    <div class="front__accent"></div>
    <div class="front__title">PRESIDENT</div>

    <div class="brand">
      <div class="brand__mark"></div>
      <div class="brand__name">MARCUS P.</div>
      <div class="brand__tag">REALTY COMPANY</div>
    </div>

    <svg class="front__band" width="540" height="309" viewBox="0 0 540 309">
      <rect x="0" y="176" width="540" height="10" fill="var(--blue)"/>
      <polygon points="0,186 540,186 540,194 0,198" fill="var(--blue-dark)"/>
      <rect x="0" y="170" width="540" height="3" fill="var(--grey-light)"/>
      <!-- home -->
      <g transform="translate(100,184)">
        <circle r="19" fill="var(--grey)" stroke="#fff" stroke-width="3"/>
        <path d="M-9,1 L0,-8 L9,1 M-6,-1 V8 H6 V-1" fill="none" stroke="#fff" stroke-width="2.2" stroke-linejoin="round"/>
      </g>
      <!-- phone -->
      <g transform="translate(270,184)">
        <circle r="19" fill="var(--grey)" stroke="#fff" stroke-width="3"/>
        <rect x="-9" y="-4" width="18" height="11" rx="2" fill="#fff"/>
        <path d="M-10,-4 Q0,-12 10,-4" fill="none" stroke="#fff" stroke-width="3" stroke-linecap="round"/>
        <circle cx="0" cy="2" r="2.5" fill="var(--grey)"/>
      </g>
      <!-- globe -->
      <g transform="translate(430,184)">
        <circle r="19" fill="var(--grey)" stroke="#fff" stroke-width="3"/>
        <g fill="none" stroke="#fff" stroke-width="1.6">
          <circle r="9"/>
          <ellipse rx="4" ry="9"/>
          <line x1="-9" y1="0" x2="9" y2="0"/>
          <line x1="-8" y1="-4.5" x2="8" y2="-4.5"/>
          <line x1="-8" y1="4.5" x2="8" y2="4.5"/>
        </g>
      </g>
    </svg>

    <address class="contact contact--address" style="font-style:normal">42 Tarrow Lane<br>Suite 115<br>East Orange, NJ 07019</address>
    <div class="contact contact--phone">+973 555 0142<br>+973 555 0187</div>
    <div class="contact contact--web">Marcus@marcusprealtyco.example<br>www.MarcusPrealtyco.example</div>
  </section>

  <section class="card card--back">
    <div class="back__brand">
      <div class="back__mark"></div>
      <div class="back__brandname">MARCUS P.</div>
    </div>
    <div class="back__band"></div>
    <div class="back__stripe"></div>
    <div class="back__name">MARCUS PELLOW</div>
    <div class="back__title">PRESIDENT</div>
  </section>

</div>
</body>
</html>
```